Below Par Parenting

I would like a poster (size to be agreed) created for the wording that I have composed and which I have pasted below. The poster is for my own personal gratification. It is not for commercial use. The message is driven by honesty and a profound sense of mea culpa. I am open to ideas regarding style and presentation.
I am an awful parent. No question. I am not cut out for this shit. I’m too quick to temper. I turn everything into a test of wills. I’m not down for food on the floor, for having my car trashed with your stink and detritus, for having the walls of my house daubed in your greasy fingerprints. I want to listen to The Marrows not Bumble Over Dewfields on repeat. I enjoyed making you but, on reflection, I should have pulled out. Let me go back in time to that great waste of space and energy that is ante-natal classes and tell that boho with the flowery dress and curly hair, ‘Why are you concentrating on the first five seconds? All the pain comes later. Why aren’t you telling us what to do when they won’t sleep, when they won’t sit in their high chairs, when they won’t sleep on the aeroplane?’ Boy, I wish I could play it loosey-goosey like those left-leaning parents I see going ‘coo-coo’ in Brindisetti’s but I’m not built like that. I am a right-wing despot. It’s Nazi Germany back at my place. I’m not interested in your meltdowns and tantrums. You want to writhe on the floor in the car park going red in the face? Make my day. You want to go spastic because I won’t let you watch TV for five hours straight? I don’t give a shit. Read my lips. I won’t pander to it. My wife says you’re babies but all I see is little people with an agenda. I’ve got naughty steps and sin-bins all over the joint. I wish I wasn’t the tyrant, the Valdrumo and the Oko Temba I am but it is what it is. I blame my parents and they, in turn, will blame me and their parents. Understand I don’t want to infect you too much with my bad behavior but if you could stop making such a scene in public places with your screaming, your bitching and your all round refusal to play nice then maybe, just maybe, we’d have a chance and I wouldn’t be such an awful parent.

```html
<!DOCTYPE html>
<html lang="en">
<head>
<meta charset="utf-8">
<title>Below Par Parenting</title>
<link rel="stylesheet" href="https://fonts.googleapis.com/css2?family=Jim+Nightshade&display=swap">
<style>
  :root {
    --paper-light: #ecebe6;
    --paper-mid: #dedcd4;
    --paper-edge: #b9b6ad;
    --rule: rgba(120, 130, 150, 0.16);
    --ink: #1b1917;
    --ink-red: #d9241b;
  }
  html, body {
    margin: 0;
    padding: 0;
    width: 933px;
    height: 1200px;
    overflow: hidden;
  }
  .poster {
    position: relative;
    width: 933px;
    height: 1200px;
    overflow: hidden;
    background:
      radial-gradient(ellipse 320px 90px at 120px 0px, rgba(70, 66, 60, 0.45), transparent 70%),
      radial-gradient(ellipse 260px 70px at 420px 0px, rgba(90, 86, 80, 0.25), transparent 70%),
      repeating-linear-gradient(to bottom, transparent 0 28px, var(--rule) 28px 29px),
      radial-gradient(ellipse at 50% 45%, var(--paper-light) 0%, var(--paper-mid) 70%, var(--paper-edge) 100%);
  }
  .confession {
    position: absolute;
    left: 72px;
    top: 66px;
    margin: 0;
    font-family: "Jim Nightshade", cursive;
    font-size: 28.5px;
    line-height: 49px;
    color: var(--ink);
  }
  .confession .line {
    display: block;
    white-space: nowrap;
  }
  .confession .outburst {
    color: var(--ink-red);
  }
</style>
</head>
<body>
<main class="poster">
  <p class="confession">
    <span class="line">I am an awful parent. No question. I am not cut out for this shit. I’m too quick to</span>
    <span class="line">temper. I turn everything into a test of wills. I’m not down for food on the floor,</span>
    <span class="line">for having my car trashed with your stink and detritus, for having the walls of my house daubed</span>
    <span class="line">in your greasy fingerprints. I want to listen to The Marrows not Bumble Over Dewfields on repeat.</span>
    <span class="line">I enjoyed making you but, on reflection, I should have pulled out.</span>
    <span class="line">Let me go back in time to that great waste of space and energy that is</span>
    <span class="line">ante-natal classes and tell that boho with the flowery dress and curly hair,</span>
    <span class="line outburst">‘Why are you concentrating on the first five seconds?</span>
    <span class="line outburst">All the pain comes later. Why aren’t you telling us what to do when they won’t sleep,</span>
    <span class="line outburst">when they won’t sit in their high chairs, when they won’t sleep on the aeroplane?’</span>
    <span class="line">Boy, I wish I could play it loosey-goosey like those left-leaning parents</span>
    <span class="line">I see going ‘coo-coo’ in Brindisetti’s but I’m not built like that. I am a right-wing</span>
    <span class="line">despot. It’s Nazi Germany back at my place. I’m not interested in your meltdowns</span>
    <span class="line">and tantrums. You want to writhe on the floor in the car park going red in the</span>
    <span class="line">face? Make my day. You want to go spastic because I won’t let you watch TV</span>
    <span class="line">for five hours straight? I don’t give a shit. Read my lips. I won’t pander to it.</span>
    <span class="line">My wife says you’re babies but all I see is little people with an agenda.</span>
    <span class="line">I’ve got naughty steps and sin-bins all over the joint. I wish I wasn’t the tyrant,</span>
    <span class="line">the Valdrumo and the Oko Temba I am but it is what it is. I blame my parents and</span>
    <span class="line">they, in turn, will blame me and their parents. Understand I don’t want to infect you too</span>
    <span class="line">much with my bad behavior but if you could stop making such a scene in public places with your</span>
    <span class="line">screaming, your bitching and your all round refusal to play nice</span>
    <span class="line">then maybe, just maybe, we’d have a chance and I wouldn’t be such an awful parent.</span>
  </p>
</main>
</body>
</html>
```